Electrical & Communications Company Wordpress Themed Website Design

Hi everyone,

I need a wordpress themed website designed for a new company based in Sydney Australia called "VELTRIX". It delivers electrical and communication services to the domestic and commercial sectors.

It needs to be the FULL/COMPLETE wordpress theme! A clean and easy to use site.

Please guys take the time to look at these competitors sites:

www.tapnovo.com.au
www.harbelwiring.com.au
www.qul.com.au
www.lumavoltics.com.au
www.corbinwiring.com.au
www.fendrasparkies.com.au

Please use these site for ideas only!!! we want to be original.

(If you would like to add electrical and communications to the logo that is O.K.)

Note: These logo's are registered trademarks of veltrix pty ltd.

Accreditation:

Ubta member (Federated wiring and signalling guild)

PLEASE CHECK THE WEB PLANNING LAYOUT BELOW FOR ROUGH IDEA
Updates

Have requested to increase payment to $400 and now guarantee payment!

Hi guys, forgot to mention i would like to see the business phone number prominently some where with a call to action.As we are a service business and need people to easly be able to see our contact number. Maybe top right courner but open to ideas. 

 Guys/Girls this is for a complete working word press theme that i can load up on the sever and access thru wordpress admin. Code etc

Industry/Entity Type

Communications

Requirements
Must have
• - Logo Provided must be used
• - Themes and colours to be consisted with with brand
• - Fully customizable
• - Have a social share button from shariq.com
• - Must be the full/complete theme for word press
Nice to have
• - pixtorvault
• - contactform
• - would like zenda orbit pay quidlo displayed
• - Guarantee logo or something
Should not have
• - Please don't waste your or our time submitting templates or copies of other sites original only!

```html
<!DOCTYPE html>
<html lang="en">
<head>
<meta charset="utf-8">
<title>VELTRIX – Electrical and Communications</title>
<link href="https://fonts.googleapis.com/css2?family=Arimo:wght@400;700&display=swap" rel="stylesheet">
<style>
:root{
  --red:#d8141b;
  --ink:#333;
  --muted:#666;
  --line:#ddd;
  --page:#e9e9e9;
  --panel:#f2f2f2;
  --footer:#1e1e1e;
  --badge:#c9c9c9;
  --white:#fff;
}
*{box-sizing:border-box;margin:0;padding:0}
html,body{width:736px;height:1200px;overflow:hidden}
body{background:var(--page);font-family:"Arimo",Arial,sans-serif;color:var(--ink);font-size:8px;line-height:1.35}
.site{position:relative;width:664px;height:1025px;margin:0 auto;background:var(--white)}
.site-header{height:64px;position:relative;padding:10px 14px}
.brand{display:flex;align-items:center;gap:6px}
.brand-dot{width:16px;height:16px;border-radius:50%;background:var(--red)}
.brand-name{font-size:26px;font-weight:700;color:var(--red);letter-spacing:1px}
.brand-tag{font-size:7px;font-weight:700;color:var(--red);margin-left:22px;margin-top:-2px}
.call{position:absolute;right:14px;top:8px;font-size:11px;font-weight:700;color:var(--muted)}
.call strong{font-size:20px;color:var(--red);margin-left:4px}
.main-nav{position:absolute;right:14px;top:38px;display:flex;font-size:9px}
.main-nav a{display:block;padding:5px 8px;color:var(--muted);text-decoration:none;border-left:1px solid var(--line)}
.main-nav a.current{background:var(--red);color:var(--white);border:0}
.hero{position:relative;height:214px;margin:0 14px;background:linear-gradient(160deg,#c9d3de 0%,#8796a8 45%,#3b4656 100%)}
.hero-text{position:absolute;right:10px;top:64px;width:250px;padding:10px 12px;background:rgba(20,24,32,.55);color:var(--white);font-size:11px;font-weight:700;line-height:1.4;text-transform:uppercase;border-left:3px solid var(--red)}
.features{display:flex;gap:10px;margin:10px 14px 0;height:96px}
.feature{flex:1;display:flex;gap:8px;padding:8px;background:linear-gradient(#fafafa,#e6e6e6);border:1px solid var(--line)}
.feature-img{flex:none;width:30px;height:78px;background:linear-gradient(#6d6d6d,#2e2e2e)}
.feature-img.callout{width:40px;background:linear-gradient(#e9e9e9,#bdbdbd);display:flex;align-items:center;justify-content:center}
.no-badge{background:var(--red);color:var(--white);font-weight:700;font-size:15px;padding:4px 3px}
.feature h3{font-size:12px;color:var(--red);margin-bottom:3px}
.feature p{font-size:7px;color:var(--muted)}
.feature .more{font-size:7px;font-weight:700;color:var(--ink);margin-top:3px;display:block}
.content{display:flex;gap:18px;margin:14px 14px 0}
.primary{width:410px}
.sidebar{width:208px}
.primary h2{font-size:15px;font-weight:700;color:var(--ink);margin:0 0 7px;padding-bottom:5px;border-bottom:1px solid var(--line)}
.primary h2 span{color:var(--red)}
.primary p{font-size:7.5px;color:var(--muted);margin-bottom:8px}
.btn{display:inline-block;background:var(--red);color:var(--white);font-size:8px;font-weight:700;padding:5px 14px;border-radius:10px;margin:2px 0 18px}
.testimonials h2{border:0;font-size:14px}
.quote{display:flex;gap:6px;margin-bottom:12px}
.quote svg{flex:none}
.panel{background:var(--panel);border:1px solid var(--line);padding:8px;margin-bottom:14px}
.sidebar h4{font-size:9px;font-weight:700;color:var(--ink);margin-bottom:6px;text-transform:uppercase}
.sidebar p{font-size:7px;color:var(--muted);margin-bottom:5px}
.field label{display:block;font-size:7px;font-weight:700;margin-bottom:2px}
.field .input{height:13px;background:var(--white);border:1px solid #ccc;margin-bottom:6px}
.field .area{height:38px}
.form-actions{display:flex;gap:6px;justify-content:center}
.form-actions .btn{margin:2px 0 0;border-radius:3px;padding:4px 12px}
.post{display:flex;gap:8px;margin-bottom:6px}
.post-img{flex:none;width:52px;height:52px;background:linear-gradient(#9fb3c8,#4d5f74)}
.post h5{font-size:10px;color:var(--ink)}
.pay{display:flex;gap:5px;align-items:center;margin-top:6px}
.pay span{display:flex;align-items:center;justify-content:center;height:20px;padding:0 5px;border:1px solid var(--line);font-size:7px;font-weight:700;color:var(--ink);background:var(--white)}
.seal{width:22px;height:22px;border-radius:50%;background:var(--red)}
.site-footer{position:absolute;left:0;top:1035px;width:736px;height:165px;background:var(--footer);color:#bbb;display:flex;padding:18px 50px;gap:40px}
.site-footer .brand-name{font-size:20px}
.copy{font-size:7px;margin-top:10px}
.contact-info h4{color:var(--white);font-size:13px;margin-bottom:5px}
.partners h4{color:var(--white);font-size:8px;margin-bottom:5px}
.contact-info p{font-size:7.5px;line-height:1.5}
.partner-badge{width:80px;height:50px;background:var(--badge);border-radius:3px}
</style>
</head>
<body>
<div class="site">
  <header class="site-header">
    <div class="brand"><span class="brand-dot"></span><span class="brand-name">VELTRIX</span></div>
    <div class="brand-tag">ELECTRICAL AND COMMUNICATIONS</div>
    <div class="call">Call Now <strong>1300 555 019</strong></div>
    <nav class="main-nav">
      <a class="current" href="#">Home</a><a href="#">About Us</a><a href="#">Products</a><a href="#">Services</a><a href="#">Blog</a><a href="#">Contact Us</a>
    </nav>
  </header>

  <section class="hero" role="img" aria-label="Photograph of tall city office towers against the sky">
    <div class="hero-text">Veltrix electrical and communication services to the domestic and commercial sectors in Sydney Australia</div>
  </section>

  <section class="features">
    <div class="feature">
      <div class="feature-img" role="img" aria-label="Photograph of an electrician at work"></div>
      <div><h3>24 x 7 A WEEK</h3><p>Lorem ipsum is simply dummy text of the printing and typesetting industry. Lorem ipsum has been the standard text.</p><span class="more">Read more</span></div>
    </div>
    <div class="feature">
      <div class="feature-img callout"><span class="no-badge">No!</span></div>
      <div><h3>CALLOUT FEE</h3><p>Lorem ipsum is simply dummy text of the printing and typesetting industry. Lorem ipsum has been the standard text.</p><span class="more">Read more</span></div>
    </div>
    <div class="feature">
      <div class="feature-img" role="img" aria-label="Photograph of electrical tools"></div>
      <div><h3>FIXED PRICING</h3><p>Lorem ipsum is simply dummy text of the printing and typesetting industry. Lorem ipsum has been the standard text.</p><span class="more">Read more</span></div>
    </div>
  </section>

  <div class="content">
    <main class="primary">
      <h2>WELCOME TO <span>VELTRIX</span></h2>
      <p>Contrary to popular belief, Lorem Ipsum is not simply random text. It has roots in a piece of classical Latin literature from 45 BC, making it over 2000 years old. A professor at a college in Virginia looked up one of the more obscure Latin words, consectetur, from a Lorem Ipsum passage, and going through the cites of the word in classical literature, discovered the undoubtable source.</p>
      <p>Lorem Ipsum comes from sections of a work on the theory of ethics, very popular during the Renaissance. The first line of Lorem Ipsum comes from a line in a section of that same work.</p>
      <p>The standard chunk of Lorem Ipsum used since the 1500s is reproduced below for those interested. Sections from the same work are also reproduced in their exact original form, accompanied by English versions from a later translation.</p>
      <h2>HEADING 1</h2>
      <p>Contrary to popular belief, Lorem Ipsum is not simply random text. It has roots in a piece of classical Latin literature from 45 BC, making it over 2000 years old. A professor at a college in Virginia looked up one of the more obscure Latin words, consectetur, and going through the cites of the word in classical literature, discovered the source.</p>
      <p>Lorem Ipsum comes from sections of a work on the theory of ethics, very popular during the Renaissance. The first line of Lorem Ipsum comes from a line in section 1.10.32.</p>
      <span class="btn">Read More</span>
      <h2>HEADING 2</h2>
      <p>Contrary to popular belief, Lorem Ipsum is not simply random text. It has roots in a piece of classical Latin literature from 45 BC, making it over 2000 years old. A professor at a college in Virginia looked up one of the more obscure Latin words, consectetur, and going through the cites of the word in classical literature, discovered the source.</p>
      <p>Lorem Ipsum comes from sections of a work on the theory of ethics, very popular during the Renaissance. The first line of Lorem Ipsum comes from a line in section 1.10.32.</p>
      <span class="btn">Read More</span>
      <section class="testimonials">
        <h2>Testimonials:</h2>
        <div class="quote"><svg width="14" height="12" viewBox="0 0 14 12"><path d="M0 12V6L4 0h2L4 6h2v6zM8 12V6l4-6h2l-2 6h2v6z" fill="#bbb"/></svg><p>It is a long established fact that a reader will be distracted by the readable content of a page when looking at its layout. The point of using Lorem Ipsum is that it has a more-or-less normal distribution of letters.</p></div>
        <div class="quote"><svg width="14" height="12" viewBox="0 0 14 12"><path d="M0 12V6L4 0h2L4 6h2v6zM8 12V6l4-6h2l-2 6h2v6z" fill="#bbb"/></svg><p>It is a long established fact that a reader will be distracted by the readable content of a page when looking at its layout. The point of using Lorem Ipsum is that it has a more-or-less normal distribution of letters.</p></div>
      </section>
    </main>

    <aside class="sidebar">
      <div class="panel">
        <h4>Contact Us Now</h4>
        <p>Please fill out the form below and we will send you a detailed estimate within 1 business day.</p>
        <div class="field"><label>Name:</label><div class="input"></div></div>
        <div class="field"><label>Email:</label><div class="input"></div></div>
        <div class="field"><label>Website URL:</label><div class="input"></div></div>
        <div class="field"><label>Phone Number:</label><div class="input"></div></div>
        <div class="field"><label>Message:</label><div class="input area"></div></div>
        <div class="form-actions"><span class="btn">Submit</span><span class="btn">Clear</span></div>
      </div>
      <div>
        <h4>Subscribe to our newsletter</h4>
        <p>Get the marketing tips that will help your business grow. Sign up today and we will send offers and the latest company news to your inbox.</p>
        <div class="field"><div class="input"></div></div>
        <span class="btn">Subscribe Now</span>
      </div>
      <div>
        <h4>Recent Blog Posts</h4>
        <div class="post">
          <div class="post-img" role="img" aria-label="Blog post thumbnail photograph"></div>
          <div><h5>Topic Ba</h5><p>11 March 2011</p><p>Lorem ipsum is simply dummy text of the printing industry.</p></div>
        </div>
        <span class="btn">More</span>
        <div class="pay"><span>zenda</span><span>orbit pay</span><span>quidlo</span><i class="seal" aria-label="Guarantee seal"></i></div>
      </div>
    </aside>
  </div>
</div>

<footer class="site-footer">
  <div>
    <div class="brand"><span class="brand-dot"></span><span class="brand-name">VELTRIX</span></div>
    <div class="brand-tag">ELECTRICAL AND COMMUNICATIONS</div>
    <p class="copy">Copyright © 2011<br>All Rights Reserved</p>
  </div>
  <div class="contact-info">
    <h4>Contact info:</h4>
    <p>12 Harbour Street, Level 2<br>Sydney NSW 2000<br>Phone: 1300 555 019</p>
  </div>
  <div class="partners">
    <h4>OUR PARTNERS</h4>
    <div class="partner-badge" role="img" aria-label="Partner association badge"></div>
  </div>
</footer>
</body>
</html>
```